Bref créative
TQR Constructors stationary
business cards,letterhead,envelopes
Simple
Norah Wilcott
President
5127 Larkspur Meadow Rd.
Highland Park, IL 60035
norah.tqr@mailbox-example.com
www.tqrconstructors-example.com
Here is our logo file. Please us it

```html
<!DOCTYPE html>
<html lang="en">
<head>
<meta charset="utf-8">
<title>TQR Constructors Stationery</title>
<link href="https://fonts.googleapis.com/css2?family=Open+Sans:wght@400;600;700;800&display=swap" rel="stylesheet">
<style>
:root{
  --bg:#eceeef;
  --paper:#ffffff;
  --paper-shade:#f2f4f6;
  --blue:#1f6fb8;
  --blue-deep:#0d3c73;
  --blue-light:#4f95d6;
  --ink:#2b2f33;
  --muted:#7b8289;
  --ghost:#e3e7eb;
  --card-dark:#4a4e52;
}
*{margin:0;padding:0;box-sizing:border-box}
html,body{width:1200px;height:574px;overflow:hidden}
body{background:var(--bg);font-family:"Open Sans",Arial,sans-serif;color:var(--ink);position:relative}
.sheet{position:absolute;background:var(--paper);box-shadow:0 1px 4px rgba(0,0,0,.18);overflow:hidden}
.brand{display:flex;align-items:center;gap:6px;font-weight:800;color:var(--blue-deep);white-space:nowrap}
.brand .mark{background:var(--blue);display:block}
.ghost-square{position:absolute;background:var(--ghost);opacity:.7}
.baseline{position:absolute;left:0;right:0;bottom:0;height:4px;background:var(--blue)}
.small-text{font-size:5.5px;color:var(--muted);white-space:nowrap}

/* envelope back */
.env-back{left:24px;top:36px;width:353px;height:139px}
.env-back .band{position:absolute;left:0;top:0;right:0;height:58px;background:linear-gradient(180deg,var(--blue-deep),var(--blue))}
.env-back svg{position:absolute;left:0;top:0}
.env-back .brand{position:absolute;left:50%;top:70px;transform:translateX(-50%);font-size:11px}
.env-back .brand .mark{width:12px;height:12px}

/* envelope front */
.env-front{left:24px;top:180px;width:353px;height:156px}
.env-front .brand{position:absolute;left:14px;top:18px;font-size:19px}
.env-front .brand .mark{width:22px;height:22px}
.env-front .return{position:absolute;left:14px;top:70px}
.env-front .corner{position:absolute;right:12px;bottom:12px;width:34px;height:34px;background:var(--blue)}

/* compliment slip */
.slip{left:24px;top:348px;width:353px;height:144px}
.slip .brand{position:absolute;left:14px;top:18px;font-size:19px}
.slip .brand .mark{width:22px;height:22px}
.slip .ghost-square{right:30px;top:38px;width:72px;height:72px}
.slip .return{position:absolute;left:14px;top:122px}

/* letterheads */
.letterhead{top:36px;width:320px;height:456px}
.lh-a{left:384px}
.lh-b{left:710px}
.letterhead .brand{position:absolute;left:50%;top:20px;transform:translateX(-50%);font-size:16px}
.letterhead .brand .mark{width:20px;height:20px}
.letterhead .ghost-square{left:50%;top:186px;width:116px;height:116px;transform:translateX(-50%)}
.letterhead .footer{position:absolute;left:0;right:0;bottom:10px;display:flex;justify-content:center;gap:10px}

/* business cards */
.card{left:1039px;width:137px}
.card-dark{top:36px;height:108px;background:linear-gradient(160deg,#5b6065,var(--card-dark))}
.card-blue{top:149px;height:91px;background:linear-gradient(160deg,var(--blue),var(--blue-deep))}
.card-dark .brand,.card-blue .brand{position:absolute;left:50%;top:50%;transform:translate(-50%,-50%);font-size:10px;color:#fff}
.card-dark .brand .mark{width:11px;height:11px;background:var(--blue-light)}
.card-blue .brand .mark{width:11px;height:11px;background:#fff}
.card-front{height:77px}
.cf-1{top:247px}.cf-2{top:331px}.cf-3{top:415px}
.card-front .person{position:absolute;left:8px;top:10px}
.card-front .name{font-size:6.5px;font-weight:700;color:var(--ink)}
.card-front .role{font-size:5px;color:var(--muted);margin-bottom:4px}
.card-front .small-text{font-size:4.2px;line-height:1.4}
.card-front .brand{position:absolute;right:6px;top:28px;font-size:6px;gap:3px}
.card-front .brand .mark{width:8px;height:8px}
.card-front .baseline{height:3px}
</style>
</head>
<body>

<section class="sheet env-back" aria-label="Envelope back">
  <div class="band"></div>
  <svg width="353" height="139" viewBox="0 0 353 139" aria-hidden="true">
    <polyline points="0,0 176.5,62 353,0" fill="none" stroke="#ffffff" stroke-width="1.5"/>
    <polygon points="0,58 0,0 176.5,62 353,0 353,58 176.5,62" fill="rgba(255,255,255,0.08)"/>
  </svg>
  <div class="brand"><span class="mark"></span>TQR Constructors</div>
</section>

<section class="sheet env-front" aria-label="Envelope front">
  <div class="brand"><span class="mark"></span>TQR Constructors</div>
  <p class="return small-text">5127 Larkspur Meadow Rd. Highland Park, IL 60035</p>
  <span class="corner"></span>
  <div class="baseline"></div>
</section>

<section class="sheet slip" aria-label="Compliment slip">
  <div class="brand"><span class="mark"></span>TQR Constructors</div>
  <span class="ghost-square"></span>
  <p class="return small-text">5127 Larkspur Meadow Rd. Highland Park, IL 60035</p>
  <div class="baseline"></div>
</section>

<section class="sheet letterhead lh-a" aria-label="Letterhead">
  <div class="brand"><span class="mark"></span>TQR Constructors</div>
  <span class="ghost-square"></span>
  <div class="footer small-text">
    <span>5127 Larkspur Meadow Rd. Highland Park, IL 60035</span>
    <span>(847) 555-0198</span>
    <span>www.tqrconstructors-example.com</span>
  </div>
  <div class="baseline"></div>
</section>

<section class="sheet letterhead lh-b" aria-label="Letterhead">
  <div class="brand"><span class="mark"></span>TQR Constructors</div>
  <span class="ghost-square"></span>
  <div class="footer small-text">
    <span>5127 Larkspur Meadow Rd. Highland Park, IL 60035</span>
    <span>(847) 555-0198</span>
    <span>norah.tqr@mailbox-example.com</span>
  </div>
  <div class="baseline"></div>
</section>

<section class="sheet card card-dark" aria-label="Business card back, dark">
  <div class="brand"><span class="mark"></span>TQR Constructors</div>
</section>

<section class="sheet card card-blue" aria-label="Business card back, blue">
  <div class="brand"><span class="mark"></span>TQR Constructors</div>
</section>

<section class="sheet card card-front cf-1" aria-label="Business card front">
  <div class="person">
    <p class="name">Norah Wilcott</p>
    <p class="role">President</p>
    <p class="small-text">5127 Larkspur Meadow Rd.</p>
    <p class="small-text">Highland Park, IL 60035</p>
    <p class="small-text">norah.tqr@mailbox-example.com</p>
    <p class="small-text">www.tqrconstructors-example.com</p>
  </div>
  <div class="brand"><span class="mark"></span>TQR</div>
  <div class="baseline"></div>
</section>

<section class="sheet card card-front cf-2" aria-label="Business card front">
  <div class="person">
    <p class="name">Norah Wilcott</p>
    <p class="role">President</p>
    <p class="small-text">5127 Larkspur Meadow Rd.</p>
    <p class="small-text">Highland Park, IL 60035</p>
    <p class="small-text">norah.tqr@mailbox-example.com</p>
    <p class="small-text">www.tqrconstructors-example.com</p>
  </div>
  <div class="brand"><span class="mark"></span>TQR</div>
  <div class="baseline"></div>
</section>

<section class="sheet card card-front cf-3" aria-label="Business card front">
  <div class="person">
    <p class="name">Norah Wilcott</p>
    <p class="role">President</p>
    <p class="small-text">5127 Larkspur Meadow Rd.</p>
    <p class="small-text">Highland Park, IL 60035</p>
    <p class="small-text">norah.tqr@mailbox-example.com</p>
    <p class="small-text">www.tqrconstructors-example.com</p>
  </div>
  <div class="brand"><span class="mark"></span>TQR</div>
  <div class="baseline"></div>
</section>

</body>
</html>
```